wardrobe/costume stylist needs good business card for own business

Hi:)

I'm wanting a business card for my company. I am a freelance stylist.

I do wardrobe/costume stylist to TV commercials; Films; Fashion and Lifestyle shoots.

I'd like a design based around my name Rosalind Pember written nicely, maybe a colour? Up to you?!

I've attached a couple of images of business cards I like
.... be creative and have fun!

Thank you :)
Updates

Reason: I was trying to get my new business card ready for before I headed overseas Friday morning but I don't think that was realistic so I'd like to extend the deadline to give time to the project. Thank you

Hi designers:) Thank you for all your designs, I've extended the deadline until Sunday, so there's a bit more time. I've attached 3 pictures of business cards which I quite like, please take a look to see if it can be of help in your process. I like the pale plain or patterned background with dark font and the dark plain or patterned background with the pale font the motifs the feminine fonts the plain fonts I like the idea of playing with a circle or some shape on one side of the card with my name or initials as in the picture I have on my post could you play around with this idea a bit please? Thank you all for the work you've done :) Rosa

Hi I am working overseas til Saturday night sorry for no feedback until I teturn Thanks :) Rosa

Hi designers, Thank you all so much for submitting your designs, I really appreciate your input into my project :) I'm sorry I didn't get to respond to some comments, and give feedback. I didn't back from being away until later than I expected, and the deadline had passed then, so apologies. Thanks to you all again for all your really good designs :) Rosa

Target Market(s)

I am a freelance stylist my target audience is producers, production companies, photographers, directors...

Industry/Entity Type

Business

Requirements
Must have
• Rosalind Pember
Stylist or Wardrobe Stylist

email rosapember@quillnet.co.nz
Mobile 0218846193

(Don't have to use the words 'email' and 'mobile')
Nice to have
• Would like it to be double sided
Like B & W
Like pale colour background with dark font or white font
Like dark colour background with pale font
Should not have
• I would prefer it not to incorporate pictures

```html
<!DOCTYPE html>
<html lang="en">
<head>
<meta charset="utf-8">
<title>Rosalind Pember – Wardrobe Stylist Business Card</title>
<link href="https://fonts.googleapis.com/css2?family=Marcellus&family=Tenor+Sans&display=swap" rel="stylesheet">
<style>
  :root {
    --page: #f4f4f4;
    --card-dark: #0d0d0d;
    --card-mid: #2a2a2a;
    --gold: #c9a13b;
    --gold-light: #e6c15a;
    --gold-deep: #8a6a1c;
  }
  * { box-sizing: border-box; margin: 0; padding: 0; }
  html, body {
    width: 1200px;
    height: 900px;
    overflow: hidden;
    background: var(--page);
  }
  .canvas {
    width: 1200px;
    height: 900px;
    display: flex;
    align-items: center;
    justify-content: center;
    gap: 40px;
  }
  .card {
    position: relative;
    width: 540px;
    height: 310px;
    border-radius: 26px;
    background: radial-gradient(ellipse at 50% 40%, var(--card-mid) 0%, var(--card-dark) 70%);
    box-shadow: 0 10px 24px rgba(0,0,0,0.18);
    display: flex;
    flex-direction: column;
    align-items: center;
    justify-content: center;
    color: var(--gold);
  }
  .card--front::before {
    content: "";
    position: absolute;
    inset: 9px;
    border: 4px solid var(--gold);
    border-radius: 20px;
    box-shadow: inset 0 0 0 1px var(--gold-deep);
  }
  .ornament {
    background: radial-gradient(ellipse at center, var(--gold-light) 0%, var(--gold) 45%, rgba(201,161,59,0) 75%);
    border-radius: 50%;
  }
  .ornament--large { width: 150px; height: 58px; }
  .ornament--small { width: 80px; height: 32px; }
  .brand-name {
    font-family: "Marcellus", serif;
    color: var(--gold);
    line-height: 1;
    letter-spacing: 1px;
  }
  .brand-role {
    font-family: "Marcellus", serif;
    color: var(--gold-deep);
    text-transform: none;
    line-height: 1;
  }
  .card--front .brand-name { font-size: 48px; margin-top: 8px; }
  .card--front .brand-role { font-size: 15px; letter-spacing: 7px; margin: 4px 0 8px; }
  .card--back { justify-content: flex-start; padding-top: 40px; }
  .card--back .brand-name { font-size: 23px; margin-top: 4px; }
  .card--back .brand-role { font-size: 8px; letter-spacing: 4px; margin: 3px 0 4px; }
  .contact {
    margin-top: 36px;
    font-family: "Tenor Sans", sans-serif;
    color: var(--gold);
    text-align: center;
    font-size: 15px;
    letter-spacing: 3px;
    line-height: 1.6;
    font-style: normal;
  }
</style>
</head>
<body>
  <main class="canvas">
    <section class="card card--front" aria-label="Business card front">
      <div class="ornament ornament--large" role="img" aria-label="Gold baroque flourish ornament"></div>
      <h1 class="brand-name">Rosalind Pember</h1>
      <p class="brand-role">Wardrobe Stylist</p>
      <div class="ornament ornament--large" role="img" aria-label="Gold baroque flourish ornament"></div>
    </section>

    <section class="card card--back" aria-label="Business card back">
      <div class="ornament ornament--small" role="img" aria-label="Gold baroque flourish ornament"></div>
      <h2 class="brand-name">Rosalind Pember</h2>
      <p class="brand-role">Wardrobe Stylist</p>
      <div class="ornament ornament--small" role="img" aria-label="Gold baroque flourish ornament"></div>
      <address class="contact">
        <div class="contact__phone">0218846193</div>
        <div class="contact__email">rosapember@quillnet.co.nz</div>
      </address>
    </section>
  </main>
</body>
</html>
```